Verdell Chiropractic, achieve your health goals, get better each day one step at a time

A mobile friendly site, fresh look, easy to navigate, has interface with pw/chirply, etc. Blog posts. Uses new logo. Content and address to current site is mirvaton.com. The current site will give you scope of project for content. The logo is not the final but close. Will upload final next week.
Convey the concept that heath is a process, it does not just happen. We take steps to achieve what we want in life including health.

Target Market(s)

30 to 70 year old. Needing health care

Industry/Entity Type

Health Care

Coding

Coded - Design and coding required

Number of Pages Required

5+ page

Font styles to use
Sans Serif

Colors

Designer to choose colors to be used in the design.

Requirements
Must have
• mobile friendly, easy to navigate, PW/Chirply interface, blog, room for current content
Nice to have
• potential for commerce, statistics
Should not have
• Same old look and feel as everything else out there

```html
<!DOCTYPE html>
<html lang="en">
<head>
<meta charset="utf-8">
<title>Verdell Chiropractic</title>
<link rel="stylesheet" href="https://fonts.googleapis.com/css2?family=Fira+Sans:wght@500;600;700&family=Fira+Sans+Condensed:wght@700&family=Mulish:wght@400;600;700&display=swap">
<style>
:root{
  --green:#9fc03b;
  --blue:#52739f;
  --blue-deep:#45658f;
  --ink:#3d3d3d;
  --muted:#707070;
  --line:#d6d6d6;
  --grey-bg:#ebebeb;
  --white:#ffffff;
}
*{margin:0;padding:0;box-sizing:border-box}
html,body{width:1200px;height:3109px;overflow:hidden}
body{position:relative;background:var(--white);font-family:"Mulish",Arial,sans-serif;color:var(--ink)}
.abs{position:absolute}
.heading{font-family:"Fira Sans",Arial,sans-serif;font-weight:700;font-size:40px;letter-spacing:-.5px;text-align:center}
.heading .accent{color:var(--green)}
.heading .main{color:var(--blue)}

/* top bar */
.topbar{left:0;top:0;width:1200px;height:42px;background:var(--green);color:var(--white);font-size:16px;display:flex;align-items:center;justify-content:flex-end;padding-right:54px;gap:12px;letter-spacing:.3px}
.topbar svg{width:20px;height:20px}

/* header */
.header{left:0;top:42px;width:1200px;height:103px;background:var(--white);box-shadow:0 2px 6px rgba(0,0,0,.06)}
.brand{left:80px;top:37px;display:flex;align-items:center;gap:10px;font-family:"Fira Sans",Arial,sans-serif;font-weight:700;font-size:22px;color:var(--blue);letter-spacing:.3px;white-space:nowrap}
.brand-dot{width:24px;height:24px;border-radius:50%;background:var(--green)}
.nav{right:64px;top:37px;display:flex;gap:4px;font-size:14px;color:var(--ink);letter-spacing:.3px;white-space:nowrap}
.nav a{padding:10px 17px;text-decoration:none;color:inherit;border:2px solid transparent}
.nav a.active{border-color:var(--green);color:var(--green)}

/* hero */
.hero{left:0;top:145px;width:1200px;height:564px;background:linear-gradient(100deg,#8fa3bf 0%,#6d86aa 40%,#7b92b3 65%,#97a9c3 100%)}
.hero-frame{left:355px;top:276px;width:494px;height:294px}
.hero-title{left:0;top:318px;width:1200px;text-align:center;font-family:"Fira Sans Condensed",Arial,sans-serif;font-weight:700;font-size:50px;line-height:60px;color:var(--white);letter-spacing:.5px}
.hero-text{left:370px;top:390px;width:460px;text-align:center;color:var(--white);font-size:15px;line-height:1.6}
.hero-btn{left:506px;top:466px;width:188px;height:46px;border:2px solid var(--green);color:var(--green);font-family:"Fira Sans",Arial,sans-serif;font-weight:600;font-size:19px;display:flex;align-items:center;justify-content:center}
.hero-arrow{top:402px;width:24px;height:36px}

/* meet */
.meet-title{left:0;top:758px;width:1200px}
.meet-card{left:201px;top:829px;width:831px;height:415px;border:2px solid var(--line);background:var(--white)}
.meet-photo{left:170px;top:860px;width:270px;height:353px;background:linear-gradient(160deg,#c9a98b 0%,#8b6a55 45%,#3c3331 100%)}
.meet-body{left:498px;top:890px;width:500px}
.meet-name{font-family:"Mulish",Arial,sans-serif;font-weight:600;font-size:22px;color:var(--blue);margin-bottom:20px}
.meet-sub{font-size:19px;font-weight:600;color:var(--ink);margin-bottom:12px}
.meet-line{font-size:14px;color:var(--muted);margin-bottom:14px}
.meet-btn{display:inline-flex;align-items:center;justify-content:center;width:188px;height:46px;border-radius:23px;background:var(--blue);color:var(--white);font-family:"Fira Sans",Arial,sans-serif;font-weight:500;font-size:19px;margin-top:14px}

/* services */
.services{left:0;top:1337px;width:1200px;height:562px;background:var(--grey-bg)}
.services-photo{left:93px;top:1372px;width:353px;height:527px;background:linear-gradient(180deg,#d8c7b8 0%,#efefef 45%,#c9c9c9 100%)}
.services-title{left:539px;top:1404px;text-align:left}
.service{width:290px;display:flex;gap:24px}
.service-icon{flex:none;width:62px;height:62px;background:var(--blue);border-radius:3px;display:flex;align-items:center;justify-content:center}
.service-icon span{width:26px;height:26px;border-radius:50%;border:4px solid var(--green)}
.service h3{font-family:"Mulish",Arial,sans-serif;font-weight:600;font-size:19px;color:var(--ink);margin-bottom:6px;line-height:1.3}
.service p{font-size:14px;color:var(--muted);line-height:1.65}

/* testimonials */
.testi{left:0;top:1899px;width:638px;height:468px;background:var(--blue)}
.testi-photo{left:638px;top:1899px;width:562px;height:468px;background:radial-gradient(circle at 55% 55%,#eaf3ff 0%,#9cc3ee 45%,#4f8fdc 100%)}
.testi-title{left:78px;top:1957px;font-family:"Fira Sans",Arial,sans-serif;font-weight:700;font-size:40px;color:var(--green)}
.testi-avatar{left:78px;top:2027px;width:96px;height:96px;border-radius:50%;background:linear-gradient(160deg,#f0c6a4,#b98062);border:3px solid rgba(255,255,255,.6)}
.testi-name{left:78px;top:2146px;font-size:16px;font-weight:700;color:var(--white)}
.testi-text{left:78px;top:2180px;width:470px;font-size:15px;line-height:1.65;color:var(--white)}
.testi-dots{left:78px;top:2275px;display:flex;gap:8px}
.testi-dots span{width:32px;height:3px;background:rgba(255,255,255,.45)}
.testi-dots span.on{background:var(--white)}

/* contact */
.contact-title{left:0;top:2414px;width:1200px}
.field{border:1px solid var(--line);border-top:none;height:42px;font-size:14px;color:var(--ink);padding:4px 20px}
.send-btn{left:506px;top:2641px;width:186px;height:46px;border:2px solid var(--green);color:var(--green);font-family:"Fira Sans",Arial,sans-serif;font-weight:600;font-size:19px;display:flex;align-items:center;justify-content:center}

/* footer */
.footer{left:0;top:2774px;width:1200px;height:273px;background:linear-gradient(100deg,#5f7fab 0%,#53739f 50%,#6684ad 100%)}
.news-label{left:0;top:2835px;width:1200px;text-align:center;color:var(--white);font-size:18px}
.news-form{left:300px;top:2881px;width:602px;height:46px;border:1px solid rgba(255,255,255,.85);border-radius:23px;display:flex;align-items:center;justify-content:space-between;padding-left:30px;color:var(--white);font-size:15px}
.news-btn{width:166px;height:46px;margin-right:-1px;border-radius:23px;background:var(--green);color:var(--white);font-family:"Fira Sans",Arial,sans-serif;font-weight:500;font-size:19px;display:flex;align-items:center;justify-content:center}
.foot-nav{left:0;top:2970px;width:1200px;display:flex;justify-content:center;color:var(--white);font-size:15px}
.foot-nav span{padding:0 26px;border-left:1px solid rgba(255,255,255,.55);line-height:14px}
.foot-nav span:first-child{border-left:none}
.copy{left:0;top:3047px;width:1200px;height:62px;background:var(--green);color:var(--white);font-size:15px;display:flex;align-items:center;justify-content:center}
</style>
</head>
<body>

<div class="abs topbar">
  <span>CALL US NOW</span>
  <svg viewBox="0 0 24 24" fill="none" stroke="#fff" stroke-width="1.6"><path d="M5 3h4l2 5-2.5 1.5a11 11 0 0 0 6 6L16 13l5 2v4a2 2 0 0 1-2 2A17 17 0 0 1 3 5a2 2 0 0 1 2-2z"/></svg>
  <span>555.014.2290</span>
</div>

<header class="abs header">
  <div class="abs brand"><span class="brand-dot"></span>VERDELL CHIROPRACTIC</div>
  <nav class="abs nav">
    <a class="active">HOME</a><a>MEET DR. HALVORSEN</a><a>TESTIMONIALS</a><a>FAQS</a><a>RESOURCES</a><a>CONTACTS</a>
  </nav>
</header>

<section class="abs hero" role="img" aria-label="Photo of a patient holding a knee with a glowing knee joint overlay, clinic backdrop and plant"></section>
<svg class="abs hero-frame" viewBox="0 0 494 294" fill="none" stroke="#fff" stroke-width="3">
  <path d="M2 30V2h28M464 2h28v28M2 264v28h28M464 292h28v-28"/>
</svg>
<svg class="abs hero-arrow" style="left:26px" viewBox="0 0 24 36" fill="none" stroke="#fff" stroke-width="4"><path d="M18 4L6 18l12 14"/></svg>
<svg class="abs hero-arrow" style="right:26px" viewBox="0 0 24 36" fill="none" stroke="#fff" stroke-width="4"><path d="M6 4l12 14L6 32"/></svg>
<h1 class="abs hero-title">KNEE PAIN</h1>
<p class="abs hero-text">Knee pain is deeply concerning to athletes. To anyone it brings thoughts of how am I going to get around if my knee gives out.</p>
<div class="abs hero-btn">KNOW MORE</div>

<h2 class="abs heading meet-title"><span class="accent">MEET</span> <span class="main">DR. HALVORSEN</span></h2>
<div class="abs meet-card"></div>
<div class="abs meet-photo" role="img" aria-label="Portrait of the doctor standing with his wife"></div>
<div class="abs meet-body">
  <p class="meet-name">Dr. Martin Halvorsen with wife Elise</p>
  <p class="meet-sub">Education</p>
  <p class="meet-line" style="margin-bottom:26px">Lone Prairie Chiropractic College 1991, Doctor of Chiropractic with honors</p>
  <p class="meet-sub">Additional Education</p>
  <p class="meet-line">Diplomate, National Council of Homeopathic Review, 1991</p>
  <p class="meet-line">Diplomate, Chiropractic Council of Clinical Nutrition, 1996</p>
  <span class="meet-btn">KNOW MORE</span>
</div>

<section class="abs services"></section>
<div class="abs services-photo" role="img" aria-label="Chiropractor adjusting the neck of a seated patient"></div>
<h2 class="abs heading services-title"><span class="accent">OUR</span> <span class="main">SERVICES</span></h2>
<div class="abs service" style="left:539px;top:1478px"><div class="service-icon"><span></span></div><div><h3>Chiropractic</h3><p>As a Chiropractor, Dr. Halvorsen focuses on disorders...</p></div></div>
<div class="abs service" style="left:842px;top:1478px"><div class="service-icon"><span></span></div><div><h3>Acupuncture</h3><p>The term “acupuncture” describes a family...</p></div></div>
<div class="abs service" style="left:539px;top:1603px"><div class="service-icon"><span></span></div><div><h3>Applied Kinesiology</h3><p>Dr. Halvorsen's practice has been centered around...</p></div></div>
<div class="abs service" style="left:842px;top:1603px"><div class="service-icon"><span></span></div><div><h3>Massage</h3><p>Marla's experience in massage and myofacial...</p></div></div>
<div class="abs service" style="left:539px;top:1717px"><div class="service-icon"><span></span></div><div><h3>Homeopathy</h3><p>Homeopathy is a system of medical therapy that...</p></div></div>
<div class="abs service" style="left:842px;top:1717px"><div class="service-icon"><span></span></div><div><h3>Spinal Decompression</h3><p>Spinal Decompression...</p></div></div>

<section class="abs testi"></section>
<div class="abs testi-photo" role="img" aria-label="Back view of a person holding the neck with the spine highlighted in red"></div>
<h2 class="abs testi-title">TESTIMONIALS</h2>
<div class="abs testi-avatar" role="img" aria-label="Client portrait"></div>
<p class="abs testi-name">- NAME SURNAME</p>
<p class="abs testi-text">Lorem Ipsum is simply dummy text of the printing and typesetting industry. Lorem Ipsum has been the industry's standard dummy text ever since the 1500s, when an unknown printer took a galley.</p>
<div class="abs testi-dots"><span class="on"></span><span></span><span></span></div>

<h2 class="abs heading contact-title"><span class="accent">CONTACT</span> <span class="main">US</span></h2>
<div class="abs field" style="left:220px;top:2479px;width:240px">Name</div>
<div class="abs field" style="left:479px;top:2479px;width:240px">Email</div>
<div class="abs field" style="left:740px;top:2479px;width:240px">Phone</div>
<div class="abs field" style="left:220px;top:2574px;width:760px;height:42px">Message</div>
<div class="abs send-btn">SEND NOW</div>

<footer class="abs footer" role="img" aria-label="Faint photo of a patient receiving spinal treatment"></footer>
<p class="abs news-label">Subscribe to our Newsletter</p>
<div class="abs news-form"><span>Enter your email</span><span class="news-btn">SUBSCRIBE</span></div>
<div class="abs foot-nav"><span>Home</span><span>Meet Dr. Halvorsen</span><span>Testimonials</span><span>FAQs</span><span>Resources</span><span>Contact us</span></div>
<div class="abs copy">©Verdell CHIROPRACTIC- 2018. All Rights Reserved.</div>

</body>
</html>
```